Gala Dinner Flyer for State Water Polo Association

We need a promotional flyer for the "2016 Coral Soirée" - a fundraising gala dinner for Tideline Aquatics League to distribute to our members.

The details for the event are as follows:

Date: Saturday 16th April 2016
Time: 7pm to Midnight
Venue: Marlow Hall B, Kestrel Wharf, 47 Fenwick Promenade, Brinlow Quay 3091
Cost: $150 per person
Details: Canapés on arrival followed by a three course dinner, with premium beverages throughout the evening.
RSVP: Friday 8th April 2016
Dress Code: Black Tie
For tickets for to www.tikvora.com.au/tickets/event/coralsoiree

We also require an event logo with a minimum height of 200px, and event background with a minimum width of 1200px and height of 800px, and flyer image with a minimum width of 620px and height of 874px.

I have attached a number of logos we need incorporated along with last years invitation and a few photos from last years event.

We would like to use designs that use water and the colour blue.

The final design should communicate elegance and high class

Target Market(s)

25-60 year old Men and Women from affluent families

Industry/Entity Type

Promotional

Colors
1861ab
3277b5
85acd3
cedeed
ffffff

Requirements
Must have
• Tideline Aquatics League Logo, Bramble Otters Logo, heartsteady Logo & Corvane Holdings Logo

```html
<!DOCTYPE html>
<html lang="en">
<head>
<meta charset="utf-8">
<title>2016 Coral Soirée – Gala Dinner Flyer</title>
<link href="https://fonts.googleapis.com/css2?family=Poiret+One&family=Great+Vibes&family=Roboto+Condensed:ital,wght@0,400;0,700;1,400;1,700&family=Open+Sans:wght@400;700&display=swap" rel="stylesheet">
<style>
  :root{
    --navy:#1861ab;
    --blue:#3277b5;
    --sky:#85acd3;
    --mist:#cedeed;
    --white:#ffffff;
    --ink:#0a0d12;
    --text-dark:#1a1a1a;
    --glow:#2a8fd8;
  }
  html,body{margin:0;padding:0;width:849px;height:1200px;overflow:hidden;background:var(--white);}
  .flyer{
    position:relative;width:849px;height:1200px;overflow:hidden;
    background:
      radial-gradient(circle at 18% 55%, rgba(50,119,181,.35) 0 40px, transparent 42px),
      radial-gradient(circle at 82% 48%, rgba(50,119,181,.28) 0 55px, transparent 57px),
      radial-gradient(circle at 65% 62%, rgba(24,97,171,.3) 0 35px, transparent 37px),
      radial-gradient(ellipse at 50% 45%, #0f2740 0%, var(--ink) 65%);
    font-family:"Open Sans",sans-serif;
  }
  .photo{position:absolute;}
  .photo--stage{left:0;top:0;width:430px;height:260px;
    background:radial-gradient(ellipse at 40% 40%, #6c7078 0%, #2a2d33 55%, rgba(10,13,18,0) 100%);}
  .photo--round{border-radius:50%;border:3px solid var(--blue);
    background:radial-gradient(circle at 45% 40%, #7a7f88 0%, #33373e 60%, #15181d 100%);}
  .photo--a{left:600px;top:-40px;width:200px;height:200px;}
  .photo--b{left:740px;top:60px;width:150px;height:150px;}
  .photo--c{left:700px;top:300px;width:160px;height:160px;}
  .rings{position:absolute;inset:0;pointer-events:none;}
  .title{position:absolute;left:0;right:0;top:150px;text-align:center;color:var(--glow);}
  .title__year{font-family:"Poiret One",sans-serif;font-size:64px;letter-spacing:6px;line-height:1;}
  .title__name{font-family:"Poiret One",sans-serif;font-size:118px;letter-spacing:10px;line-height:1;margin-top:6px;}
  .title__script{font-family:"Great Vibes",cursive;color:var(--white);font-size:120px;line-height:1;margin-top:-14px;padding-left:180px;}
  .date-ribbon{position:absolute;left:0;top:482px;width:849px;height:95px;}
  .date-ribbon__text{position:absolute;left:95px;top:504px;font-family:"Roboto Condensed",sans-serif;font-style:italic;font-weight:700;
    font-size:44px;color:var(--white);letter-spacing:1px;transform:rotate(-3deg);transform-origin:left;white-space:nowrap;}
  .details{position:absolute;left:60px;top:605px;width:735px;}
  .detail{position:relative;display:flex;align-items:center;height:56px;margin-bottom:11px;}
  .detail--tall{height:64px;}
  .detail__label{position:relative;z-index:2;width:210px;height:100%;display:flex;align-items:center;padding-left:34px;box-sizing:border-box;
    font-family:"Roboto Condensed",sans-serif;font-style:italic;font-size:30px;color:var(--white);letter-spacing:1px;
    background:linear-gradient(180deg,var(--sky) 0%,var(--blue) 45%,var(--navy) 100%);
    clip-path:polygon(0 0,88% 0,100% 50%,88% 100%,0 100%,6% 50%);}
  .detail__value{flex:1;margin-left:-14px;height:84%;background:var(--white);display:flex;flex-direction:column;justify-content:center;align-items:center;
    text-align:center;color:var(--text-dark);font-family:"Open Sans",sans-serif;font-weight:700;font-size:19px;padding:0 16px;}
  .detail__sub{font-weight:400;font-size:12px;}
  .detail__small{font-weight:400;font-size:12px;line-height:1.35;}
  .tickets{position:absolute;left:0;right:0;top:1030px;margin:0;text-align:center;font-family:"Open Sans",sans-serif;font-weight:700;font-size:21px;color:var(--white);}
  .tickets__lead{color:var(--glow);margin-right:6px;}
  .sponsors{position:absolute;left:40px;right:40px;bottom:30px;height:80px;background:var(--white);display:flex;align-items:center;justify-content:space-around;}
  .sponsor{font-family:"Roboto Condensed",sans-serif;font-weight:700;font-size:17px;color:var(--navy);display:flex;align-items:center;gap:8px;}
  .sponsor__dot{width:16px;height:16px;border-radius:50%;background:var(--navy);}
</style>
</head>
<body>
<main class="flyer">
  <div class="photo photo--stage" role="img" aria-label="Photo of performers on stage at last year's gala"></div>
  <div class="photo photo--round photo--a" role="img" aria-label="Photo of guests dining at last year's gala"></div>
  <div class="photo photo--round photo--b" role="img" aria-label="Photo of the decorated gala room"></div>
  <div class="photo photo--round photo--c" role="img" aria-label="Photo of guests dancing at last year's gala"></div>

  <svg class="rings" width="849" height="1200" viewBox="0 0 849 1200" aria-hidden="true">
    <g fill="none" stroke="#3277b5" stroke-width="2" opacity=".8">
      <circle cx="110" cy="470" r="62"/>
      <circle cx="760" cy="640" r="90"/>
      <circle cx="600" cy="110" r="40"/>
      <circle cx="55" cy="320" r="36"/>
    </g>
  </svg>

  <header class="title">
    <div class="title__year">2016</div>
    <div class="title__name">CORAL</div>
    <div class="title__script">Soirée</div>
  </header>

  <svg class="date-ribbon" viewBox="0 0 849 95" aria-hidden="true">
    <defs>
      <linearGradient id="ribbonFill" x1="0" y1="0" x2="0" y2="1">
        <stop offset="0" stop-color="#85acd3"/>
        <stop offset=".5" stop-color="#3277b5"/>
        <stop offset="1" stop-color="#1861ab"/>
      </linearGradient>
    </defs>
    <polygon points="720,8 800,4 780,42 805,80 735,70" fill="#0f3e70"/>
    <polygon points="0,30 760,0 760,60 0,95" fill="url(#ribbonFill)"/>
  </svg>
  <div class="date-ribbon__text">SATURDAY 16TH APRIL 2016</div>

  <section class="details">
    <div class="detail"><div class="detail__label">TIME</div><div class="detail__value">7.00PM TILL MIDNIGHT</div></div>
    <div class="detail"><div class="detail__label">VENUE</div><div class="detail__value">MARLOW HALL B, KESTREL WHARF<span class="detail__sub">47 Fenwick Promenade, Brinlow Quay 3091</span></div></div>
    <div class="detail detail--tall"><div class="detail__label">DETAILS</div><div class="detail__value"><span class="detail__small">Canapés on arrival followed by a three course dinner,<br>with premium beverages throughout the evening.</span></div></div>
    <div class="detail"><div class="detail__label">COST</div><div class="detail__value">$150 PER PERSON</div></div>
    <div class="detail"><div class="detail__label">DRESS</div><div class="detail__value">BLACK TIE</div></div>
    <div class="detail"><div class="detail__label">RSVP</div><div class="detail__value">FRIDAY 8TH APRIL 2016</div></div>
  </section>

  <p class="tickets"><span class="tickets__lead">FOR TICKETS GO TO</span>www.tikvora.com.au/tickets/event/coralsoiree</p>

  <footer class="sponsors">
    <span class="sponsor"><span class="sponsor__dot"></span>Bramble Otters</span>
    <span class="sponsor">Tideline Aquatics League</span>
    <span class="sponsor">heartsteady</span>
    <span class="sponsor">Corvane Holdings</span>
  </footer>
</main>
</body>
</html>
```